Bright Acorn day Nursery flyer

I need a great flyer to attract new parents. Bright Acorn Is a fantastic, warm and homely nursery in Westmere road SE6 London. We offer many things that other nurseries don't offer such as Spanish, Yoga, Music, Cooking classes and Signwise. We also have an amazing system called KINDTRAK that allows parents to get alerts on the KINDTRAK app about their children daily activities and even developmental reports. Parents are able to share with the nursery great moments and put pictures and videos through the app. We also offer the parent camera, an extremely safe system that allows parents to log in and see their children whilst they are engaged in exciting activities.
Full details of Nursery
87 Westmere road
SE6 4QP
02084417260
www.brightacornhollis.co.uk
facebook page
brightacorndaynursery@brightacornhollis.co.uk
Updates

double sided or mini brochure type

Hi Please keep it simple and clean I feel the designs are a good attempt thank you but they are very busy and I just want to add important points a lot of the designs have too many colours, too much text etc Thank you!

https://www.facebook.com/brightacornhollis.co.uk/

Target Market(s)

parents of children 0-5

Industry/Entity Type

Childcare

Colors

Designer to choose colors to be used in the design.

Requirements
Must have
• colour and pictures but clean design

```html
<!DOCTYPE html>
<html lang="en">
<head>
<meta charset="utf-8">
<title>Bright Acorn day Nursery flyer</title>
<link rel="stylesheet" href="https://fonts.googleapis.com/css2?family=Quicksand:wght@500;600&family=Courier+Prime:wght@700&family=Montserrat:wght@700&display=swap">
<style>
  :root {
    --card: #ffffff;
    --ink: #1c1c1c;
    --brand-teal: #1aa89a;
    --address-green: #3d9b3d;
    --balloon-red: #f2452e;
    --balloon-yellow: #f7c21a;
    --balloon-teal: #2fb7c4;
    --balloon-pink: #f26d9b;
    --balloon-green: #8cc63f;
    --badge: #f7a21a;
  }
  * { margin: 0; padding: 0; box-sizing: border-box; }
  html, body { width: 857px; height: 1200px; overflow: hidden; }
  body { position: relative; background: var(--card); }

  .balloon-backdrop {
    position: absolute; inset: 0;
    background:
      radial-gradient(circle at 8% 10%, var(--balloon-red) 0 12%, transparent 22%),
      radial-gradient(circle at 92% 6%, var(--balloon-yellow) 0 14%, transparent 24%),
      radial-gradient(circle at 96% 45%, var(--balloon-teal) 0 12%, transparent 22%),
      radial-gradient(circle at 4% 55%, var(--balloon-green) 0 12%, transparent 22%),
      radial-gradient(circle at 10% 95%, var(--balloon-teal) 0 14%, transparent 24%),
      radial-gradient(circle at 90% 96%, var(--balloon-pink) 0 14%, transparent 24%),
      radial-gradient(circle at 50% 100%, var(--balloon-yellow) 0 12%, transparent 22%),
      linear-gradient(135deg, var(--balloon-yellow), var(--balloon-pink) 40%, var(--balloon-teal) 75%, var(--balloon-yellow));
  }

  .flyer-card {
    position: absolute;
    left: 68px; top: 68px;
    width: 718px; height: 1075px;
    background: var(--card);
  }

  .brand {
    position: absolute;
    left: 0; right: 0; top: 150px;
    text-align: center;
  }
  .brand-dot {
    display: block;
    width: 120px; height: 120px;
    margin: 0 auto 40px;
    border-radius: 50%;
    background: var(--badge);
  }
  .brand-name {
    font-family: "Quicksand", sans-serif;
    font-weight: 600;
    font-size: 66px;
    line-height: 1.1;
    color: var(--brand-teal);
  }

  .intro {
    position: absolute;
    left: 86px; width: 570px; top: 522px;
    font-family: "Quicksand", sans-serif;
    font-weight: 500;
    font-size: 19.5px;
    line-height: 22.6px;
    color: var(--ink);
  }

  .address {
    position: absolute;
    left: 120px; width: 420px; top: 895px;
    text-align: center;
    font-family: "Courier Prime", monospace;
    font-weight: 700;
    font-size: 18px;
    line-height: 25px;
    color: var(--address-green);
    font-style: normal;
  }

  .website {
    position: absolute;
    left: 0; right: 0; top: 1002px;
    text-align: center;
    font-family: "Montserrat", sans-serif;
    font-weight: 700;
    font-size: 21px;
    color: #000;
  }
</style>
</head>
<body>
  <div class="balloon-backdrop" role="img" aria-label="Close-up of colourful party balloons in red, yellow, teal, pink and green"></div>

  <main class="flyer-card">
    <header class="brand">
      <span class="brand-dot"></span>
      <h1 class="brand-name">Bright Acorn<br>day Nursery</h1>
    </header>

    <p class="intro">Bright Acorn is a fantastic, warm and homely nursery in Westmere road SE6 London. We offer many things that other nurseries don't offer such as Spanish, Yoga, Music, Cooking classes and Signwise. We also have an amazing system called KINDTRAK that allows parents to get alerts on the KINDTRAK app about their children daily activities and even developmental reports. Parents are able to share with the nursery great moments and put pictures and videos through the app. We also offer the parent camera, an extremely safe system that allows parents to log in and see their children whilst they are engaged in exciting activities.</p>

    <address class="address">
      87 Westmere road<br>
      SE6 4QP<br>
      02084417260
    </address>

    <p class="website">WWW.BRIGHTACORNHOLLIS.CO.UK</p>
  </main>
</body>
</html>
```